Food Safety Consultancy Flyer Design

We need a flyer design for a new company called Tundo Training. New food safety regulations are coming into effect for all food operators in March 2016. My company provides training and resources to support food operators during the transition onto the new Food Control Plan. For the designs we would like to see any of the colours used from the logo which is attached. The flyer will be letting operators know that there are new regulations and we are here to help. Our company offers three packages: 1. Videos (training videos) 2. Webinars and Workshop 3. One-on-one mentoring. Our websites main colour used is the green colour from the logo.
Food service operators: cafes, restaurants etc.
Hospitality

```html
<!DOCTYPE html>
<html lang="en">
<head>
<meta charset="utf-8">
<title>Tundo Training – Food Act 2014 Flyer</title>
<link rel="stylesheet" href="https://fonts.googleapis.com/css2?family=Open+Sans:wght@300;400;600;700&family=Oswald:wght@700&family=Fira+Sans+Condensed:wght@600&family=Dancing+Script:wght@500&display=swap">
<style>
  :root {
    --orange: #e8951f;
    --green: #3cb54a;
    --blue: #1a76bd;
    --grey-band: #d1d3d4;
    --ink: #2e2e2e;
    --muted: #555;
    --white: #ffffff;
    --bullet: #f0a02a;
  }
  * { margin: 0; padding: 0; box-sizing: border-box; }
  html, body { width: 934px; height: 1200px; overflow: hidden; background: var(--white); }
  body { font-family: "Open Sans", sans-serif; color: var(--ink); position: relative; }

  .header { position: absolute; left: 0; top: 0; width: 934px; height: 222px; }
  .brand {
    position: absolute; left: 42px; top: 86px;
    display: flex; align-items: center; gap: 14px;
    font-family: "Open Sans", sans-serif; font-weight: 700; font-size: 40px;
    color: var(--ink); letter-spacing: 1px;
  }
  .brand-dot { width: 34px; height: 34px; border-radius: 50%; background: var(--green); flex: none; }
  .intro {
    position: absolute; right: 52px; top: 44px; width: 440px;
    text-align: right; font-weight: 300; font-size: 23px; line-height: 38px; color: var(--muted);
  }

  .tagline-band {
    position: absolute; left: 0; top: 223px; width: 934px; height: 42px;
    background: var(--grey-band);
    font-family: "Dancing Script", cursive; font-size: 30px; color: var(--ink);
    padding-left: 40px; line-height: 44px;
  }

  .announcement {
    position: absolute; left: 0; top: 265px; width: 934px; height: 415px;
    background: var(--blue); color: var(--white);
  }
  .announcement-title {
    position: absolute; left: 42px; top: 14px; width: 860px;
    font-family: "Oswald", sans-serif; font-weight: 700; font-size: 60px; line-height: 68px;
    text-shadow: 0 2px 3px rgba(0,0,0,0.25);
  }
  .knowledge-heading { position: absolute; left: 42px; top: 177px; font-weight: 700; font-size: 20px; }
  .knowledge-list { position: absolute; left: 42px; top: 210px; list-style: none; }
  .knowledge-list li {
    font-weight: 300; font-size: 19px; line-height: 31.5px;
    display: flex; align-items: center; gap: 10px;
  }
  .knowledge-list li::before {
    content: ""; width: 15px; height: 15px; border-radius: 50%; background: var(--bullet); flex: none;
  }
  .transition-note { position: absolute; left: 42px; top: 373px; font-weight: 300; font-size: 18.5px; }
  .chefs-illustration {
    position: absolute; left: 410px; top: 175px; width: 486px; height: 168px;
  }

  .divider { position: absolute; left: 0; top: 680px; width: 934px; height: 8px; background: var(--grey-band); }

  .packages-title {
    position: absolute; left: 0; top: 694px; width: 934px; text-align: center;
    font-size: 46px; font-weight: 400; color: var(--blue);
  }
  .package {
    position: absolute; top: 756px; height: 318px;
    border-radius: 92px; border: 5px solid #f3f3f3;
    box-shadow: 0 3px 8px rgba(0,0,0,0.35);
    color: var(--white); text-align: center; padding: 10px 10px 0;
  }
  .package-videos { left: 60px; width: 236px; background: var(--orange); }
  .package-webinars { left: 328px; width: 286px; background: var(--green); }
  .package-mentoring { left: 639px; width: 236px; background: var(--blue); }
  .package h3 {
    font-family: "Fira Sans Condensed", sans-serif; font-weight: 600; font-size: 30px; line-height: 34px;
    padding: 6px 0 8px; margin: 0 6px; border-bottom: 1px solid rgba(255,255,255,0.6);
  }
  .package p {
    font-size: 19px; line-height: 26px; padding: 7px 0; margin: 0 6px;
    border-bottom: 1px solid rgba(255,255,255,0.6); white-space: nowrap;
  }
  .package p:last-child { border-bottom: none; }
  .package-webinars p { font-size: 16.5px; line-height: 23px; padding: 6px 0; }
  .package-webinars h3 { line-height: 36px; }
  .package-mentoring p { font-size: 21px; line-height: 34px; padding-top: 10px; }

  .website {
    position: absolute; left: 0; top: 1080px; width: 934px; text-align: center;
    font-size: 44px; color: var(--blue);
  }
  .email {
    position: absolute; left: 0; top: 1144px; width: 934px; text-align: center;
    font-size: 24px; color: var(--ink);
  }
</style>
</head>
<body>
  <header class="header">
    <div class="brand"><span class="brand-dot"></span>Tundo Training</div>
    <p class="intro">Food service and food retailers will be on Food Control Plans – documentation of processes and risk management to produce safe and suitable food.</p>
  </header>

  <div class="tagline-band">Tundo Training: Your reputation is our business</div>

  <section class="announcement">
    <h1 class="announcement-title">THE FOOD ACT 2014 Comes into force on 1 March 2016</h1>
    <h2 class="knowledge-heading">With up-to-date knowledge on:</h2>
    <ul class="knowledge-list">
      <li>The Food Act 2014</li>
      <li>Food Control Plan requirements</li>
      <li>Verification expectations</li>
      <li>New Food Grading system</li>
      <li>New Fees</li>
    </ul>
    <p class="transition-note">Let us help you transition and understand all there is to know</p>
    <svg class="chefs-illustration" role="img" aria-label="Illustration of four cartoon chefs holding vegetables, utensils, a pot and a serving cloche" viewBox="0 0 486 168">
      <defs>
        <linearGradient id="chefTone" x1="0" y1="0" x2="0" y2="1">
          <stop offset="0" stop-color="#e9eef3"/>
          <stop offset="1" stop-color="#b9c6d2"/>
        </linearGradient>
      </defs>
      <rect width="486" height="168" rx="10" fill="url(#chefTone)" opacity="0.35"/>
    </svg>
  </section>

  <div class="divider"></div>

  <h2 class="packages-title">Our packages:</h2>

  <article class="package package-videos">
    <h3>Videos</h3>
    <p>Animated training<br>videos of the FCP</p>
    <p>6 month subscription</p>
    <p>Translated into<br>Mandarin, Japanese,<br>Korean and Hindi</p>
  </article>

  <article class="package package-webinars">
    <h3>Webinars/<br>Workshops</h3>
    <p>A range of webinars at times<br>to suit the hospitality industry</p>
    <p>AND half day training<br>workshops.</p>
    <p>6 month subscription to the<br>video library is included</p>
  </article>

  <article class="package package-mentoring">
    <h3>One-to-<br>one<br>mentoring</h3>
    <p>We come to<br>you and go<br>through the FCP<br>page-by-page</p>
  </article>

  <div class="website">www.tundotraining.co.nz</div>
  <div class="email">email: info@tundotraining.co.nz</div>
</body>
</html>
```